CBD Company needs bag design made

Our company is creating CBD gummies which we need a design based off the dimensions of the AI file provided. I have included some base designs for basic ideas. The flavors are as follows "Blue Raspberry" .. "Tropical Fruit" .. "Zestplum" (which is a sour strawberry) and "Watermelon" I included the mock ups of the bags as well as some zoomed in pictures of two the labels as well to give a little better of a reference. Our company name is Brightwave which we would like instead of Dunlets (Brightwave logo attached). The final design should display what's in each bag (4 separate bag designs) with images depicting that in addition the to Brightwve Logo(ai attached). I attached the nutritional facts as well which should match the color schemes of each flavor (where the blue color is in the image attached to match the flavor example: Blue Raspberry = blue) this will be located on the back of the bag.

```html
<!DOCTYPE html>
<html lang="en">
<head>
<meta charset="utf-8">
<title>Brightwave CBD Gummies – Pouch Range</title>
<link rel="stylesheet" href="https://fonts.googleapis.com/css2?family=Lilita+One&family=Russo+One&family=Open+Sans:wght@400;700&display=swap">
<style>
  :root{
    --page:#ececec;
    --ink:#111111;
    --white:#ffffff;
    --brand-text:#5f7268;
    --label-line:#c9c9c9;
    --badge:#0d0d0d;

    --blue:#1d80c1;   --blue-stripe:#cfe6f6;  --blue-a:#6d9fd8;  --blue-b:#2f5fae;
    --plum:#a43c80;   --plum-stripe:#e6d3e6;  --plum-a:#e79acb;  --plum-b:#9c3f82;
    --orange:#ec8a2e; --orange-stripe:#f6e3c2;--orange-a:#f7b06a;--orange-b:#c7642a;
    --red:#e45b5e;    --red-stripe:#f3d0d6;   --red-a:#f28a8f;   --red-b:#c23546;
  }
  *{box-sizing:border-box;margin:0;padding:0}
  html,body{width:1200px;height:706px;overflow:hidden;background:var(--page)}
  .range{position:relative;width:1200px;height:706px}

  .pouch{
    position:absolute;top:106px;width:264px;height:478px;
    border-radius:10px 10px 14px 14px;overflow:hidden;
    background:repeating-linear-gradient(90deg,var(--stripe) 0 7px,var(--white) 7px 15px);
    box-shadow:0 6px 18px rgba(0,0,0,.12);
  }
  .pouch--blue  {left:70px; --accent:var(--blue);  --stripe:var(--blue-stripe);  --photo-a:var(--blue-a);  --photo-b:var(--blue-b)}
  .pouch--plum  {left:338px;--accent:var(--plum);  --stripe:var(--plum-stripe);  --photo-a:var(--plum-a);  --photo-b:var(--plum-b)}
  .pouch--orange{left:606px;--accent:var(--orange);--stripe:var(--orange-stripe);--photo-a:var(--orange-a);--photo-b:var(--orange-b)}
  .pouch--red   {left:874px;--accent:var(--red);   --stripe:var(--red-stripe);   --photo-a:var(--red-a);   --photo-b:var(--red-b)}

  .hang-hole{position:absolute;top:22px;left:50%;width:20px;height:20px;margin-left:-10px;border-radius:50%;background:var(--page)}

  .gummy-photo{
    position:absolute;left:24px;top:150px;width:218px;height:238px;
    background:radial-gradient(circle at 40% 35%,var(--photo-a),var(--photo-b));
  }

  .dose-badge{
    position:absolute;left:10px;top:134px;width:52px;height:52px;border-radius:50%;
    background:var(--badge);color:var(--white);z-index:2;
    font:400 11px/1.05 "Russo One",sans-serif;text-align:center;
    display:flex;flex-direction:column;justify-content:center;transform:rotate(-8deg);
  }

  .label-diamond{position:absolute;left:7px;top:24px;width:204px;height:154px}

  .brand-name{
    position:absolute;top:70px;left:0;width:100%;text-align:center;
    font:400 12px/1 "Open Sans",sans-serif;color:var(--brand-text);
  }
  .flavor-name{
    position:absolute;top:101px;left:0;width:100%;text-align:center;
    font:400 10.5px/1 "Russo One",sans-serif;color:var(--accent);letter-spacing:.3px;
  }
  .product-title{
    position:absolute;top:116px;left:0;width:100%;text-align:center;
    font:400 24px/1 "Lilita One",sans-serif;color:var(--ink);letter-spacing:.5px;
    -webkit-text-stroke:5px var(--white);paint-order:stroke fill;
  }
  .fruit-art{
    position:absolute;top:146px;left:74px;width:70px;height:34px;border-radius:14px;
    background:linear-gradient(120deg,var(--photo-a),var(--accent));
  }
  .extract-ribbon{
    position:absolute;top:212px;left:30px;width:158px;height:15px;
    background:var(--white);color:var(--ink);text-align:center;
    font:700 8.5px/15px "Open Sans",sans-serif;
    clip-path:polygon(0 0,100% 0,97% 50%,100% 100%,0 100%,3% 50%);
  }

  .serving-band{
    position:absolute;left:0;right:0;bottom:0;height:92px;background:var(--accent);
    color:var(--white);text-align:center;padding:18px 30px 0;
  }
  .serving-info{font:400 7.5px/1 "Russo One",sans-serif;letter-spacing:.1px;white-space:nowrap}
  .net-weight{margin-top:16px;font:400 6.5px/1 "Open Sans",sans-serif;opacity:.95}
</style>
</head>
<body>
<main class="range">

  <article class="pouch pouch--blue">
    <span class="hang-hole"></span>
    <div class="gummy-photo" role="img" aria-label="Close-up photo of sugar-coated blue raspberry gummy cubes">
      <svg class="label-diamond" viewBox="0 0 204 154"><polygon points="102,8 196,77 102,146 8,77" fill="#fff" stroke="#fff" stroke-width="12" stroke-linejoin="round"/><polygon points="102,16 186,77 102,138 18,77" fill="none" stroke="var(--label-line)" stroke-width="1" stroke-linejoin="round"/></svg>
      <div class="brand-name">Brightwave</div>
      <div class="flavor-name">BLUE RASPBERRY</div>
      <h2 class="product-title">CBD GUMMIES</h2>
      <div class="fruit-art" role="img" aria-label="Blue gummies with raspberry and blackberry"></div>
      <div class="extract-ribbon">High Clarity CBD extract</div>
    </div>
    <div class="dose-badge"><span>250mg</span><span>CBD</span></div>
    <div class="serving-band">
      <p class="serving-info">1 PIECE PER SERVING – 10 SERVINGS PER PACKAGE</p>
      <p class="net-weight">Net weight 2.5 oz, 70g</p>
    </div>
  </article>

  <article class="pouch pouch--plum">
    <span class="hang-hole"></span>
    <div class="gummy-photo" role="img" aria-label="Close-up photo of sugar-coated pink gummy cubes">
      <svg class="label-diamond" viewBox="0 0 204 154"><polygon points="102,8 196,77 102,146 8,77" fill="#fff" stroke="#fff" stroke-width="12" stroke-linejoin="round"/><polygon points="102,16 186,77 102,138 18,77" fill="none" stroke="var(--label-line)" stroke-width="1" stroke-linejoin="round"/></svg>
      <div class="brand-name">Brightwave</div>
      <div class="flavor-name">ZESTPLUM</div>
      <h2 class="product-title">CBD GUMMIES</h2>
      <div class="fruit-art" role="img" aria-label="Pink gummies with strawberries"></div>
      <div class="extract-ribbon">High Clarity CBD extract</div>
    </div>
    <div class="dose-badge"><span>250mg</span><span>CBD</span></div>
    <div class="serving-band">
      <p class="serving-info">1 PIECE PER SERVING – 10 SERVINGS PER PACKAGE</p>
      <p class="net-weight">Net weight 2.5 oz, 70g</p>
    </div>
  </article>

  <article class="pouch pouch--orange">
    <span class="hang-hole"></span>
    <div class="gummy-photo" role="img" aria-label="Close-up photo of sugar-coated orange gummy cubes">
      <svg class="label-diamond" viewBox="0 0 204 154"><polygon points="102,8 196,77 102,146 8,77" fill="#fff" stroke="#fff" stroke-width="12" stroke-linejoin="round"/><polygon points="102,16 186,77 102,138 18,77" fill="none" stroke="var(--label-line)" stroke-width="1" stroke-linejoin="round"/></svg>
      <div class="brand-name">Brightwave</div>
      <div class="flavor-name">TROPICAL FRUIT</div>
      <h2 class="product-title">CBD GUMMIES</h2>
      <div class="fruit-art" role="img" aria-label="Orange gummies with pineapple, peach and citrus"></div>
      <div class="extract-ribbon">High Clarity CBD extract</div>
    </div>
    <div class="dose-badge"><span>250mg</span><span>CBD</span></div>
    <div class="serving-band">
      <p class="serving-info">1 PIECE PER SERVING – 10 SERVINGS PER PACKAGE</p>
      <p class="net-weight">Net weight 2.5 oz, 70g</p>
    </div>
  </article>

  <article class="pouch pouch--red">
    <span class="hang-hole"></span>
    <div class="gummy-photo" role="img" aria-label="Close-up photo of sugar-coated red gummy cubes">
      <svg class="label-diamond" viewBox="0 0 204 154"><polygon points="102,8 196,77 102,146 8,77" fill="#fff" stroke="#fff" stroke-width="12" stroke-linejoin="round"/><polygon points="102,16 186,77 102,138 18,77" fill="none" stroke="var(--label-line)" stroke-width="1" stroke-linejoin="round"/></svg>
      <div class="brand-name">Brightwave</div>
      <div class="flavor-name">WATERMELON</div>
      <h2 class="product-title">CBD GUMMIES</h2>
      <div class="fruit-art" role="img" aria-label="Red gummies with watermelon slices"></div>
      <div class="extract-ribbon">High Clarity CBD extract</div>
    </div>
    <div class="dose-badge"><span>250mg</span><span>CBD</span></div>
    <div class="serving-band">
      <p class="serving-info">1 PIECE PER SERVING – 10 SERVINGS PER PACKAGE</p>
      <p class="net-weight">Net weight 2.5 oz, 70g</p>
    </div>
  </article>

</main>
</body>
</html>
```